Scholar Pathways - educational consulting

I am beginning an SCHOLAR PATHWAYS business - focusing on Tribal (Native American Indian) Communities, but will work with anyone. I have work experience in K-12 and Higher Education. Special Education - transition from school to work. Advising and facilitating with academic skills in higher education. I have a BS - Special Education, Masters - Educational Administration and working on a PhD in Higher Education. Also completing QMR approved certification as an Academic Life Coach

Target Market(s)

K12 college bound students and parents, Trbal Crossings college bound students and families, special education college bound students and parents

Industry/Entity Type

Business

Contact Information for Business Card

Dorena Lyle Fassett. PO Box 417, Cushing, OK 74023. (918) 555-0283. dorena@scholarpathwaysmail.net

Requirements
Must have
• Scholar Pathways is the name of the business - Trbal Crossings is a focus area
Nice to have
• Tourquoise would be nice. I do not have a logo yet

```html
<!DOCTYPE html>
<html lang="en">
<head>
<meta charset="utf-8">
<title>Scholar Pathways – Business Card</title>
<link rel="stylesheet" href="https://fonts.googleapis.com/css2?family=Open+Sans:wght@700&family=Alegreya:wght@400&display=swap">
<style>
  :root {
    --backdrop: #e9e6e1;
    --card: #0d0d0d;
    --card-edge: #1c1c1c;
    --ink-light: #f2f2f2;
    --ink-soft: #d9d9d9;
    --accent: #3fb54a;
    --faint: rgba(255,255,255,0.05);
  }
  * { box-sizing: border-box; margin: 0; padding: 0; }
  html, body {
    width: 1200px; height: 900px; overflow: hidden;
    background: var(--backdrop);
  }
  .sheet {
    width: 1200px; height: 900px;
    display: flex; flex-direction: column;
    align-items: center; justify-content: center; gap: 50px;
  }
  .card {
    position: relative;
    width: 600px; height: 343px;
    background: radial-gradient(ellipse at 60% 30%, var(--card-edge), var(--card) 70%);
    overflow: hidden;
    box-shadow: 0 10px 24px rgba(0,0,0,0.25);
  }
  /* Front */
  .card--front { display: flex; align-items: center; justify-content: center; gap: 24px; }
  .brand-dot {
    width: 78px; height: 78px; border-radius: 50%;
    background: var(--ink-light);
  }
  .brand-name {
    font-family: "Open Sans", sans-serif; font-weight: 700;
    font-size: 36px; line-height: 1.05; letter-spacing: 0.5px;
    color: var(--ink-light); text-transform: uppercase;
  }
  /* Back */
  .faint-mark {
    position: absolute; left: -70px; top: 20px;
    width: 240px; height: 240px; border-radius: 50%;
    border: 34px solid var(--faint);
  }
  .corner-dot {
    position: absolute; right: 60px; top: 36px;
    width: 120px; height: 120px; border-radius: 50%;
    background: var(--accent);
  }
  .contact {
    position: absolute; left: 56px; bottom: 40px;
    font-family: "Alegreya", serif; color: var(--ink-soft);
  }
  .contact__name { font-size: 30px; color: var(--ink-light); line-height: 1.1; }
  .contact__role { font-size: 18px; color: var(--accent); margin-bottom: 34px; }
  .contact__line { font-size: 16px; line-height: 1.6; }
  .label, .web { color: var(--accent); }
  .gap { display: inline-block; width: 10px; }
</style>
</head>
<body>
<main class="sheet">
  <section class="card card--front" aria-label="Business card front">
    <span class="brand-dot"></span>
    <h1 class="brand-name">Scholar<br>Pathways</h1>
  </section>

  <section class="card card--back" aria-label="Business card back">
    <span class="faint-mark"></span>
    <span class="corner-dot"></span>
    <div class="contact">
      <p class="contact__name">Dorena Lyle Fassett</p>
      <p class="contact__role">Educational Consultant</p>
      <p class="contact__line">PO Box 417, Cushing, OK 74023</p>
      <p class="contact__line"><span class="label">T:</span> (918) 555-0283<span class="gap"></span><span class="label">F:</span> (918) 555-0284<span class="gap"></span><span class="label">M:</span> (918) 555-0285</p>
      <p class="contact__line"><span class="label">E:</span> dorena@scholarpathwaysmail.net<span class="gap"></span><span class="web">www.scholarpathways.net</span></p>
    </div>
  </section>
</main>
</body>
</html>
```